Business card for Northland's Blue Wagon.

Good day i am looking for a business card design for my business.
The name of the business is Northland's Blue Wagon. It is a van rental business that provides a driver and helper to the customer. Customer have use to van for small moves, studio or 1 bedroom, Moving furniture like couch or kitchen cabinets.
We are available evenings, weekends and holidays.
the means to contact us is by phone at 628-947-2071; By emails at Oakridge@northlandsbluewagon.net; or by social media, Facebook and Instagram.
You can see attached pictures of the van and or logo.

```html
<!DOCTYPE html>
<html lang="en">
<head>
<meta charset="utf-8">
<title>Northland's Blue Wagon – Business Card</title>
<link rel="stylesheet" href="https://fonts.googleapis.com/css2?family=Montserrat:wght@400;600&display=swap">
<style>
  :root {
    --backdrop: #6b6b6b;
    --paper: #ffffff;
    --ink: #070708;
    --signal-red: #d2232a;
    --card-w: 867px;
    --card-h: 509px;
  }
  * { margin: 0; padding: 0; box-sizing: border-box; }
  html, body {
    width: 1200px;
    height: 1200px;
    overflow: hidden;
    background: var(--backdrop);
    font-family: "Montserrat", Arial, sans-serif;
  }
  .card {
    position: absolute;
    left: 166px;
    width: var(--card-w);
    height: var(--card-h);
    background: var(--paper);
    overflow: hidden;
    box-shadow: 3px 4px 8px rgba(0, 0, 0, 0.35);
  }
  .card--front { top: 74px; }
  .card--back { top: 629px; }
  .card__graphics {
    position: absolute;
    inset: 0;
    width: 100%;
    height: 100%;
  }
  .fill-ink { fill: var(--ink); }
  .fill-red { fill: var(--signal-red); }
  .fill-paper { fill: var(--paper); }

  .brand {
    position: absolute;
    display: flex;
    align-items: center;
    gap: 14px;
    color: var(--ink);
    font-weight: 600;
    line-height: 1.15;
  }
  .brand__mark {
    flex: none;
    background: var(--signal-red);
  }
  .card--front .brand {
    left: 62px;
    top: 118px;
    width: 260px;
    font-size: 27px;
  }
  .card--front .brand__mark { width: 22px; height: 22px; }
  .card--back .brand {
    left: 88px;
    top: 168px;
    width: 360px;
    font-size: 38px;
  }
  .card--back .brand__mark { width: 30px; height: 30px; }

  .contact {
    position: absolute;
    right: 60px;
    top: 320px;
    list-style: none;
    text-align: right;
  }
  .contact__item {
    display: flex;
    justify-content: flex-end;
    align-items: center;
    gap: 14px;
    height: 40px;
    font-size: 24px;
    font-weight: 400;
    color: var(--paper);
    letter-spacing: 0.2px;
  }
  .contact__item--web { color: var(--signal-red); }
  .contact__icon {
    width: 18px;
    height: 18px;
    flex: none;
  }
</style>
</head>
<body>

<section class="card card--front" aria-label="Business card front">
  <svg class="card__graphics" viewBox="0 0 693 407" preserveAspectRatio="none" aria-hidden="true">
    <polygon class="fill-ink" points="134,407 447,0 693,0 693,407"/>
    <polygon class="fill-red" points="347,216 693,216 520,0"/>
    <polygon class="fill-red" points="580,0 693,0 693,40 660,106"/>
    <polygon class="fill-paper" points="642,216 693,216 693,271"/>
  </svg>

  <div class="brand">
    <span class="brand__mark"></span>
    <span class="brand__name">Northland's Blue Wagon</span>
  </div>

  <ul class="contact">
    <li class="contact__item">
      <span>628-947-2071</span>
      <svg class="contact__icon" viewBox="0 0 24 24" aria-hidden="true">
        <path fill="#fff" d="M6.6 10.8c1.4 2.8 3.8 5.1 6.6 6.6l2.2-2.2c.3-.3.7-.4 1-.2 1.1.4 2.3.6 3.6.6.6 0 1 .4 1 1V20c0 .6-.4 1-1 1C10.6 21 3 13.4 3 4c0-.6.4-1 1-1h3.5c.6 0 1 .4 1 1 0 1.3.2 2.5.6 3.6.1.3 0 .7-.2 1l-2.3 2.2z"/>
      </svg>
    </li>
    <li class="contact__item">
      <span>Oakridge@northlandsbluewagon.net</span>
      <svg class="contact__icon" viewBox="0 0 24 24" aria-hidden="true">
        <rect x="2" y="5" width="20" height="14" rx="1.5" fill="#fff"/>
        <polyline points="3,6 12,13 21,6" fill="none" stroke="#070708" stroke-width="1.8"/>
      </svg>
    </li>
    <li class="contact__item contact__item--web">
      <span>northlandsbluewagon.net</span>
      <svg class="contact__icon" viewBox="0 0 24 24" aria-hidden="true">
        <circle cx="12" cy="12" r="9" fill="#d2232a"/>
        <g fill="none" stroke="#070708" stroke-width="1.2">
          <ellipse cx="12" cy="12" rx="4" ry="9"/>
          <line x1="3" y1="12" x2="21" y2="12"/>
          <line x1="12" y1="3" x2="12" y2="21"/>
        </g>
      </svg>
    </li>
  </ul>
</section>

<section class="card card--back" aria-label="Business card back">
  <svg class="card__graphics" viewBox="0 0 693 407" preserveAspectRatio="none" aria-hidden="true">
    <polygon class="fill-ink" points="357,0 442,0 632,200 693,120 693,407 367,407"/>
    <polygon class="fill-red" points="582,0 693,0 693,80 632,200"/>
    <polygon class="fill-red" points="367,407 548,165 660,407"/>
  </svg>

  <div class="brand">
    <span class="brand__mark"></span>
    <span class="brand__name">Northland's Blue Wagon</span>
  </div>
</section>

</body>
</html>
```